依頼詳細
ホームページのロゴを使いたいです。デリケートな問題ですが、事前に考え、ぜひ終活のお話をきき、
エンディングノートを一緒に書きたくなるような内容。H25年11月、9,10日の産業祭や、ポスティングで使います。
ですが、そこから繋がりができ、御葬儀の依頼をふやしたいです。
終活のイメージは、ホームページのブログの手と手を繋ぐ絵でお願したいです。
記載項目
あおば典礼(ロゴ) キャッチコピー 『大切な人を見送る方々とともに・・・まごころをこめて・・・』
〒317-0088 茨城県日立市緑苑町8-27-3
電話0294-58-7261 FAX0294-43-3540
ホームページ、あおば典礼 検索 フェイスブックページ
御葬儀の内容、金額等
終活相談会の実施、個別、グループで依頼、場所は御自宅、集会所、あおば典礼事務所でも定期的に実施しています。(ホームページ内ブログ、フェイスブックページ、事務所外掲示板、お電話にてご確認下さい。
サイズ
A4
ページ数
両面
希望イメージ
シンプル 複雑
単色 カラフル
暗い 明るい
日常 高級
遊び心 厳粛
未来的 伝統的
女性的 男性的
希望する色
紫、ピンク、
納品ファイル
• 高解像度JPG (.jpg)
補足説明
あおば典礼のホームページ参考にして下さい。
お世話になります。
終活と、御葬儀の宣伝も入れて下さい。

toriyoshiさんの提案は、お葬儀の事と、終活のこと、会社の売り、私どもの気持ちを汲んだ内容が、よくホームページやファイルを読み込んでくれていたと思いました。

お世話になりました。
初めての依頼で要領が分からず、提案しずらかったと思います。
沢山の提案をいただき、自分達が気づかなかった会社の特徴も分かりました。
lanternflyさんには、質問していただいた内容に、すぐに対応して
修正した提案をあげてもらい、ありがたい気持ちです。
会員様へ送っている、瓦版でしたらlanternflyさんの提案が親近感あってよかったと思います。皆さん、きれいに仕上げてくださり ありがとうございました。
また、何か機会がありましたら その時は宜しくお願い申しあげます。

```html
<!DOCTYPE html>
<html lang="ja">
<head>
<meta charset="utf-8">
<title>あおば典礼 ご案内</title>
<link href="https://fonts.googleapis.com/css2?family=Noto+Sans+JP:wght@400;700&family=Noto+Serif+JP:wght@500;700;900&display=swap" rel="stylesheet">
<style>
:root{
  --pink:#e8417f;
  --pink-deep:#d12a6a;
  --pink-soft:#f7c6da;
  --pink-pale:#fdeef4;
  --ink:#333;
  --grey:#666;
  --white:#fff;
}
*{margin:0;padding:0;box-sizing:border-box}
html,body{width:849px;height:1200px;overflow:hidden;background:var(--white)}
.page{position:relative;width:849px;height:1200px;overflow:hidden;font-family:"Noto Sans JP",sans-serif;color:var(--ink);
  background:linear-gradient(180deg,var(--pink-pale) 0,#fbd9e7 40%,#f8cfe0 77%,var(--white) 77.6%)}
.blossom-wash{position:absolute;inset:0 0 23% 0;
  background:radial-gradient(circle at 8% 10%,rgba(255,255,255,.85) 0 60px,transparent 120px),
  radial-gradient(circle at 90% 30%,rgba(255,255,255,.7) 0 50px,transparent 110px),
  radial-gradient(circle at 12% 78%,rgba(255,255,255,.6) 0 40px,transparent 100px),
  radial-gradient(circle at 85% 70%,rgba(255,255,255,.5) 0 40px,transparent 90px)}
.tagline{position:absolute;left:60px;top:22px;font-family:"Noto Serif JP",serif;font-weight:700;color:var(--pink);text-shadow:0 0 6px #fff}
.tagline .l1{font-size:38px;letter-spacing:1px}
.tagline .l2{font-size:38px;margin-left:290px;margin-top:6px}
.brand{position:absolute;left:0;right:0;top:160px;text-align:center;font-family:"Noto Serif JP",serif;font-weight:900;font-size:70px;color:var(--pink);letter-spacing:6px}
.brand .dot{display:inline-block;width:46px;height:46px;border-radius:50%;background:var(--pink);vertical-align:middle;margin-right:18px;position:relative;top:-6px}
.intro{position:absolute;left:32px;top:285px;width:785px;height:360px;background:var(--white);border-radius:20px;box-shadow:0 2px 8px rgba(200,80,130,.2)}
.intro-lead{position:absolute;left:40px;top:24px;width:520px;color:var(--pink-deep);font-weight:700;font-size:13.5px;line-height:1.6;white-space:nowrap}
.intro-body{position:absolute;left:40px;top:80px;width:515px;font-size:11.5px;line-height:1.75;color:var(--ink)}
.intro-body p+p{margin-top:6px}
.portrait{position:absolute;left:568px;top:30px;width:190px;height:200px;background:linear-gradient(180deg,#d9d4cf,#3b3f4a)}
.portrait-caption{position:absolute;left:558px;top:236px;width:210px;font-size:10px;line-height:1.6;color:var(--grey)}
.portrait-caption b{font-size:15px;color:var(--ink);margin-left:6px}
.message{position:absolute;left:60px;top:670px;width:190px;height:190px;border-radius:50%;background:var(--white);border:3px solid var(--pink-soft);display:flex;align-items:center;justify-content:center;text-align:center;color:var(--pink-deep);font-family:"Noto Serif JP",serif;font-weight:700;font-size:15px;line-height:1.7}
.consult{position:absolute;left:290px;top:730px;width:260px;height:100px;background:var(--white);border:2px solid var(--pink);border-radius:10px;display:flex;align-items:center;justify-content:center;text-align:center;color:var(--pink-deep);font-weight:700;font-size:14px;line-height:1.6}
.note-book{position:absolute;left:605px;top:680px;width:190px;height:140px;background:linear-gradient(135deg,#f4e6ec,#c98aa5)}
.note-caption{position:absolute;left:605px;top:826px;width:190px;text-align:center;font-size:11px;color:var(--grey)}
.footer-brand{position:absolute;left:60px;top:955px;font-family:"Noto Serif JP",serif;font-weight:900;font-size:36px;color:var(--pink);letter-spacing:3px;line-height:1.3}
.footer-brand .dot{display:inline-block;width:26px;height:26px;border-radius:50%;background:var(--pink);vertical-align:middle;margin-right:10px;position:relative;top:-4px}
.search{position:absolute;left:300px;top:965px;display:flex;height:30px;border:1px solid #aaa;font-size:13px}
.search .field{width:150px;padding:5px 8px}
.search .btn{width:56px;background:#eee;border-left:1px solid #aaa;display:flex;align-items:center;justify-content:center}
.contact{position:absolute;left:60px;top:1018px;font-size:13px;line-height:1.75;color:var(--ink)}
.contact strong{font-size:15px}
.services{position:absolute;left:580px;top:960px;width:240px;height:200px;border:1px solid var(--pink-soft);border-radius:6px;padding:14px 12px;display:grid;grid-template-columns:1fr 1fr;align-content:space-between;gap:2px 10px;font-size:12.5px;line-height:1.7}
.services li{list-style:none}
.services li::before{content:"";display:inline-block;width:9px;height:9px;background:var(--pink);margin-right:5px}
</style>
</head>
<body>
<div class="page">
  <div class="blossom-wash" role="img" aria-label="淡い桜の花びらが舞う背景"></div>
  <div class="tagline">
    <div class="l1">大切な人を見送る方々とともに</div>
    <div class="l2">まごころをこめて・・・</div>
  </div>
  <div class="brand"><span class="dot"></span>あおば典礼</div>

  <section class="intro">
    <div class="intro-lead">終活セミナーで、ちょこっと幸せになりませんか？<br>楽しく　自分らしく　人生ライフを考えエンディングノートに記しませんか？</div>
    <div class="intro-body">
      <p>あおば典礼は地域の皆様に寄り添い、心のこもったお見送りを大切にしてまいりました。日々のご相談を通して、準備の大切さを強く感じております。</p>
      <p>今、私どもが取り組んでいるのが終活のお手伝いです。元気なうちに自分の想いを整理し、家族へ伝えることで、残される方の負担が軽くなり、ご自身も安心して毎日を過ごすことができます。</p>
      <p>終活相談会はご自宅、集会所、事務所などで個別・グループどちらでも開催しております。エンディングノートの書き方から葬儀のご相談まで、お気軽にお声がけください。</p>
      <p>私たちはこれからも、大切な人を見送る方々とともに歩んでまいります。</p>
    </div>
    <div class="portrait" role="img" aria-label="代表者のスーツ姿の写真"></div>
    <div class="portrait-caption">日立生まれ 葬祭ディレクター<br>終活アドバイザー<b>代表　青葉 誠一</b></div>
  </section>

  <div class="message">大切な人へ、<br>そして自分のために<br>『ありがとう』を<br>伝える活動が<br>終活です。</div>
  <div class="consult">終活についての<br>ご相談承っております。<br>詳しくは裏面をご覧下さい。</div>
  <div class="note-book" role="img" aria-label="エンディングノートの冊子写真"></div>
  <div class="note-caption">エンディングノート</div>

  <div class="footer-brand"><span class="dot"></span>あおば典礼</div>
  <div class="search"><span class="field">あおば典礼</span><span class="btn">検索</span></div>
  <div class="contact">
    〒317-0088 茨城県日立市緑苑町8-27-3<br>
    <strong>TEL：0294-58-7261　FAX：0294-58-7269</strong><br>
    ホームページ：http://www.aoba-tenrei.example/<br>
    facebook：https://facebook.example/aobatenrei<br>
    まきおブログ：http://blog.example/aoba7261/
  </div>
  <ul class="services">
    <li>事業案内</li><li>法事・仕出し</li>
    <li>葬儀社</li><li>墓石・霊園</li>
    <li>寝台車</li><li>会葬礼状</li>
    <li>霊柩車</li><li>生花・花輪</li>
    <li>葬祭用品</li><li>仏壇・仏具</li>
  </ul>
</div>
</body>
</html>
```